Design for a real estate wev portal

Contents and features of the site
---------------------------------
Website in 5 languages: French, Dutch, English, German, Spanish.
English name of the site: Lantern Nest Living
Main purpose of the site:
- allow people to rent their house/ appartment for flatsharing purposes.
- help people wanting to find a room in flatsharing
- help people to find additional roommates for their flatsharing
Key interaction sequence:
1. I create a "group" of people who have common interest/hobbies
2. People who have the same interests/hobbies join my group
3. I look for a house/appartment to host my group
Website structure will be the following:
- Home
- Groups
-- Look for a group
--- Join a group
-- Create a group
- Properties
-- Look for a house/appartement
-- Apply
- Sales conditions
- Contact
- My account
-- My profile
-- My groups OR my properties
Your mission
------------
The client has no graphical guidelines, simply a logo (see attached).
We need a (responsive compliant) design for the following pages (we expect PSD's from you. No HTML nor CSS):
1. homepage (see example and wireframe attached)
2. properties search result list (see wireframe attached)
3. "detailed" form for properties
4. groups search result list
5. "detailed" form for groups
6. my account page
FOR THE COMPETITION step we only expect from you the design of first 2 screens.
Based on that, we will select the designer who will win the project, and will have to design the 4 remaining screens.
Target Market(s)
B2C
Industry/Entity Type
Real Estate
Number of Pages Required
5+ page
Look and feel
Each slider illustrates characteristics of the customer's brand and the style your logo design should communicate.

```html
<!DOCTYPE html>
<html lang="en">
<head>
<meta charset="utf-8">
<title>Lantern Nest Living</title>
<link href="https://fonts.googleapis.com/css2?family=Oswald:wght@300;400;500&family=Roboto:wght@400;500;700&family=Raleway:wght@500;600&display=swap" rel="stylesheet">
<style>
:root{
  --teal:#1fb3c8;
  --teal-dark:#168fa0;
  --green:#5cb947;
  --green-dark:#3f9b35;
  --ink:#333;
  --muted:#777;
  --grey-panel:#e2e2e2;
  --footer:#2b2c2e;
  --footer-deep:#1f2022;
  --white:#fff;
}
*{box-sizing:border-box;margin:0;padding:0}
html,body{width:1200px;height:2364px;overflow:hidden;background:var(--white)}
body{font-family:'Roboto',sans-serif;color:var(--ink);position:relative}
.abs{position:absolute}
.ph{position:absolute}

/* top bar */
.social-bar{left:249px;top:0;width:93px;height:19px;background:var(--teal-dark);display:flex;gap:7px;align-items:center;justify-content:center}
.social-bar span{width:8px;height:8px;border-radius:50%;background:var(--white)}
.account-bar{left:847px;top:0;display:flex;height:19px}
.account-bar a{display:block;width:52px;font:500 10px 'Roboto',sans-serif;line-height:19px;text-align:center;color:var(--white);text-decoration:none}
.btn-create{background:var(--green)}
.btn-login{background:var(--teal-dark)}

/* nav */
.main-nav{top:32px;font:500 10.5px 'Raleway',sans-serif;display:flex;gap:15px;color:var(--ink)}
.main-nav.left{left:393px}
.main-nav.right{left:676px}
.main-nav .active{color:var(--green);border-bottom:2px solid var(--green);padding-bottom:3px}
.logo-disc{left:544px;top:20px;width:112px;height:90px;border-radius:0 0 56px 56px;background:var(--white);box-shadow:0 4px 8px rgba(0,0,0,.18);z-index:3;display:flex;align-items:center;justify-content:center;flex-direction:column;gap:3px}
.logo-disc .dot{width:8px;height:8px;border-radius:50%;background:var(--green)}
.logo-disc .name{font:500 11px 'Oswald',sans-serif;line-height:1.1;color:var(--ink);text-align:center;width:80px}

/* hero */
.hero-bg{left:0;top:55px;width:1200px;height:670px;background:
  linear-gradient(180deg,rgba(250,250,250,0) 40%,#f7f7f7 100%),
  linear-gradient(90deg,#b9bfc6 0%,#dfe3e7 22%,#eef1f4 50%,#dfe4e9 78%,#c9d3dc 100%)}
.hero-slide{left:249px;top:57px;width:702px;height:331px;background:
  linear-gradient(180deg,rgba(0,0,0,0) 55%,rgba(40,34,30,.35) 100%),
  linear-gradient(180deg,#4d5763 0%,#8e96a0 30%,#a9a59c 52%,#7c6d5d 68%,#4c4a48 84%,#2f3236 100%)}
.slide-arrow{top:195px;width:14px;height:36px;background:var(--white);display:flex;align-items:center;justify-content:center;color:var(--teal);font-size:10px}
.slide-copy{left:580px;top:176px;width:340px;color:var(--white)}
.slide-copy h1{font:400 20px 'Oswald',sans-serif;color:var(--teal);margin-bottom:8px}
.slide-copy p{font:400 9px 'Roboto',sans-serif;line-height:1.45}
.btn-teal{display:inline-flex;align-items:center;gap:4px;background:var(--teal);color:var(--white);font:500 10px 'Oswald',sans-serif;padding:0 10px;height:24px}
.slide-copy .btn-teal{margin-top:16px}

/* intro cards */
.intro-card{top:445px;width:347px;height:252px;background:var(--white);box-shadow:0 1px 6px rgba(0,0,0,.35);padding:10px 8px}
.intro-card h2{font:400 16px 'Oswald',sans-serif;color:var(--teal);text-align:center;margin-bottom:10px}
.intro-pair{display:flex;gap:7px}
.intro-tile{position:relative;width:162px;height:184px;border:2px solid var(--green)}
.intro-tile .ph{inset:0}
.tile-label{position:absolute;left:0;right:0;bottom:0;height:26px;background:var(--green);color:var(--white);font:500 10px 'Oswald',sans-serif;display:flex;align-items:center;justify-content:center}
.advertise{position:absolute;left:0;right:0;bottom:0;height:134px;background:var(--green);clip-path:polygon(0 28%,50% 0,100% 28%,100% 100%,0 100%);color:var(--white);text-align:center;padding:46px 10px 0}
.advertise strong{display:block;font:500 10px 'Oswald',sans-serif;margin-bottom:8px;border-bottom:1px solid rgba(255,255,255,.7);padding-bottom:6px}
.advertise p{font:400 7px 'Roboto',sans-serif;line-height:1.4}

/* spotlight */
.section-title{font:400 20px 'Oswald',sans-serif;color:var(--teal-dark)}
.spot-card{width:347px;height:147px;background:linear-gradient(90deg,#4e9e3c,#77c257 60%,#5cb947);overflow:hidden}
.spot-card .photo{position:absolute;left:0;top:0;width:160px;height:147px;clip-path:polygon(0 0,78% 0,100% 50%,78% 100%,0 100%)}
.spot-card .frame{position:absolute;left:120px;top:8px;right:6px;bottom:8px;border:2px solid var(--white)}
.spot-card .body{position:absolute;left:164px;top:16px;width:170px;color:var(--white)}
.spot-card h3{font:400 15px 'Oswald',sans-serif;color:#1d1d1d;text-transform:uppercase}
.spot-card .rule{width:95px;height:2px;background:var(--teal);margin:6px 0 10px}
.spot-card p{font:400 9px 'Roboto',sans-serif;line-height:1.9}
.spot-card b{font-weight:700}

/* teal band */
.teal-band{left:0;top:1183px;width:1200px;height:303px;background:linear-gradient(180deg,rgba(31,179,200,.9),rgba(26,166,186,.95)),linear-gradient(90deg,#8fc9d2,#4fb9c9)}
.ksp-box{top:1243px;width:331px;height:181px;border:1px solid rgba(0,0,0,.22);background:rgba(0,0,0,.05);text-align:center;padding:28px 22px 0;color:#103c44}
.ksp-box h3{font:400 14px 'Oswald',sans-serif;color:var(--white);margin-bottom:18px}
.ksp-box p{font:400 8.5px 'Roboto',sans-serif;line-height:1.85}

/* info */
.info-grey{left:0;top:1538px;width:640px;height:406px;background:var(--grey-panel);clip-path:polygon(0 0,100% 0,96% 100%,0 100%)}
.info-photo{left:617px;top:1538px;width:583px;height:406px;background:linear-gradient(120deg,#c9a98a,#8e6d52 45%,#e2cdb2);clip-path:polygon(4% 0,100% 0,100% 100%,0 100%)}
.info-copy{left:249px;top:1590px;width:345px}
.info-copy h2{font:400 15px 'Oswald',sans-serif;color:var(--green-dark);margin-bottom:32px}
.faq{font:400 10px 'Roboto',sans-serif;line-height:1.6;color:var(--ink)}
.faq b{color:var(--teal-dark)}
.read-more{display:block;font:500 8.5px 'Oswald',sans-serif;color:var(--teal-dark);margin-top:4px}
.faq-sep{width:296px;height:1px;background:#bdbdbd;margin:14px 0 14px}

/* tabs */
.tab-teal{left:0;top:2000px;width:1200px;height:58px;background:var(--teal-dark)}
.tab-teal span{position:absolute;left:721px;top:0;height:58px;display:flex;align-items:center;color:var(--white);font:500 14px 'Oswald',sans-serif}
.tab-green{left:0;top:2000px;width:639px;height:58px;background:var(--green);clip-path:polygon(0 0,96.5% 0,100% 50%,96.5% 100%,0 100%);color:var(--white);font:500 14px 'Oswald',sans-serif;display:flex;align-items:center;justify-content:flex-end;padding-right:58px}

/* footer */
.site-footer{left:0;top:2058px;width:1200px;height:227px;background:var(--footer);color:#b6b6b6}
.f-col{position:absolute;top:32px;width:210px}
.f-col h4{font:700 9px 'Roboto',sans-serif;color:var(--white);letter-spacing:.4px;margin-bottom:22px}
.f-col p{font:400 8.5px 'Roboto',sans-serif;line-height:1.75}
.f-col address{font:italic 500 8.5px 'Roboto',sans-serif;line-height:1.75;color:var(--white);margin-top:12px}
.thumbs{display:grid;grid-template-columns:repeat(4,44px);gap:7px 7px}
.thumbs i{display:block;width:44px;height:44px}
.bottom-nav{left:0;top:2285px;width:1200px;height:51px;background:var(--footer-deep)}
.bottom-nav nav{position:absolute;left:249px;top:20px;display:flex;gap:13px;font:400 9px 'Roboto',sans-serif;color:#66686b}
.bottom-nav nav .active{color:var(--green)}
.bottom-logo{position:absolute;left:880px;top:16px;display:flex;align-items:center;gap:5px;font:500 10px 'Oswald',sans-serif;color:var(--white)}
.bottom-logo i{width:7px;height:7px;border-radius:50%;background:var(--white)}
.copyright{left:0;top:2336px;width:1200px;height:28px;background:var(--teal-dark);color:var(--white);font:400 8.5px 'Roboto',sans-serif;line-height:28px;text-align:center}
</style>
</head>
<body>

<div class="abs hero-bg" role="img" aria-label="Faded city skyline with a businessman looking through binoculars"></div>

<div class="abs social-bar"><span></span><span></span><span></span><span></span></div>
<div class="abs account-bar"><a class="btn-create">Create</a><a class="btn-login">Login</a></div>

<nav class="abs main-nav left"><span class="active">Home</span><span>Group</span><span>Properties</span></nav>
<div class="abs logo-disc"><span class="dot"></span><span class="name">Lantern Nest Living</span></div>
<nav class="abs main-nav right"><span>Sales conditions</span><span>My account</span><span>Contact</span></nav>

<div class="abs hero-slide" role="img" aria-label="Businessman standing on a rooftop overlooking a city under a cloudy sky"></div>
<div class="abs slide-arrow" style="left:249px">&#8592;</div>
<div class="abs slide-arrow" style="left:937px">&#8594;</div>
<div class="abs slide-copy">
  <h1>Flatshring for Everyone !</h1>
  <p>Lorem Ipsum is simply dummy text of the printing and typesetting industry. Lorem Ipsum has been the industry's standard dummy text ever since the 1500s, when an unknown printer took a galley of type</p>
  <span class="btn-teal">Search Now
    <svg width="9" height="9" viewBox="0 0 10 10"><circle cx="4" cy="4" r="3" fill="none" stroke="#fff" stroke-width="1.4"/><line x1="6.2" y1="6.2" x2="9" y2="9" stroke="#fff" stroke-width="1.4"/></svg></span>
</div>

<section class="abs intro-card" style="left:249px">
  <h2>Searching for accommodation</h2>
  <div class="intro-pair">
    <div class="intro-tile"><div class="ph" role="img" aria-label="Bright hotel bedroom with a large bed" style="background:linear-gradient(160deg,#b9c8d2,#d7c4ad 55%,#a4826a)"></div><div class="tile-label">I want to rent a room right now !</div></div>
    <div class="intro-tile"><div class="ph" role="img" aria-label="Modern bedroom with a stone feature wall" style="background:linear-gradient(160deg,#8e8a84,#cfc8bd 60%,#6e6a64)"></div><div class="tile-label">I want to join a group</div></div>
  </div>
</section>

<section class="abs intro-card" style="left:604px">
  <h2>I have a house for rent</h2>
  <div class="intro-pair">
    <div class="intro-tile"><div class="ph" role="img" aria-label="Yellow suburban house with a red roof" style="background:linear-gradient(180deg,#8ab7e0,#d9b24a 50%,#8a4a32)"></div>
      <div class="advertise"><strong>I WANT TO ADVERTISE !</strong><p>Lorem Ipsum is simply dummy text of the printing and typesetting industry. Lorem Ipsum has been the industry's standard dummy text ever since the 1500s, when an</p></div></div>
    <div class="intro-tile"><div class="ph" role="img" aria-label="Dark blue house lit at dusk" style="background:linear-gradient(180deg,#3d5d8c,#3b4556 55%,#8a6a3e)"></div><div class="tile-label">Why is flatsharing interesting to me ?</div></div>
  </div>
</section>

<h2 class="abs section-title" style="left:249px;top:743px">Under the spotlight</h2>
<h2 class="abs section-title" style="left:602px;top:743px">Under the Spotlight</h2>

<article class="abs spot-card" style="left:249px;top:789px">
  <div class="photo" role="img" aria-label="Group of young friends walking on a beach" style="background:linear-gradient(150deg,#8fb6d8,#c8a684 60%,#6d5a48)"></div>
  <div class="frame"></div>
  <div class="body"><h3>A nice grop</h3><div class="rule"></div><p>young worker, seeking for accomodation downtown<br><b>Average age</b> : 35 years<br>Men and women welcome</p></div>
</article>
<article class="abs spot-card" style="left:604px;top:789px">
  <div class="photo" role="img" aria-label="White family house with a green lawn" style="background:linear-gradient(180deg,#8cb3dc,#d8dbe0 50%,#4f8e3a)"></div>
  <div class="frame"></div>
  <div class="body"><h3>House</h3><div class="rule"></div><p>town<br>Rent per month<br>availability</p></div>
</article>
<article class="abs spot-card" style="left:249px;top:946px">
  <div class="photo" role="img" aria-label="Smiling group of students posing together" style="background:linear-gradient(150deg,#d6d6d6,#c98a6a 55%,#7a3b3b)"></div>
  <div class="frame"></div>
  <div class="body"><h3>Aonther nice group</h3><div class="rule"></div><p>young ladies, studying at University seeking for accomodation close to<br><b>Average age</b> : 20 years<br>Only women welcome</p></div>
</article>
<article class="abs spot-card" style="left:604px;top:946px">
  <div class="photo" role="img" aria-label="Living room apartment with red accents" style="background:linear-gradient(150deg,#c9a27a,#a8362e 55%,#6e5040)"></div>
  <div class="frame"></div>
  <div class="body"><h3>Appartment</h3><div class="rule"></div><p>town<br>Rent per month<br>availability</p></div>
</article>

<span class="abs btn-teal" style="left:508px;top:1104px">See More Groups &#10140;</span>
<span class="abs btn-teal" style="left:863px;top:1104px">See More Groups &#10140;</span>

<div class="abs teal-band" role="img" aria-label="Bright modern open-plan interior tinted in teal"></div>
<section class="abs ksp-box" style="left:257px">
  <h3>Key Selling Points for the Roommates</h3>
  <p>Lorem Ipsum is simply dummy text of the printing and typesetting industry. Lorem Ipsum has been the industry's standard dummy text ever since the 1500s, when an unknown printer took a galley of type and scrambled it to make a type specimen book. It has survived not only Lorem Ipsum is simply dummy text of the printing and typesetting industry. Lorem Ipsum has been the industry's standard dummy text ever since the 1500s, when an unknown printer took a</p>
</section>
<section class="abs ksp-box" style="left:612px">
  <h3>Key Selling Points for the Owners</h3>
  <p>Lorem Ipsum is simply dummy text of the printing and typesetting industry. Lorem Ipsum has been the industry's standard dummy text ever since the 1500s, when an unknown printer took a galley of type and scrambled it to make a type specimen book. It has survived not only Lorem Ipsum is simply dummy text of the printing and typesetting industry. Lorem Ipsum has been the industry's standard dummy text ever since the 1500s, when an unknown printer took a</p>
</section>

<div class="abs info-grey"></div>
<div class="abs info-photo" role="img" aria-label="Three friends laughing together at a cafe table"></div>
<section class="abs info-copy">
  <h2>Everything You need to know About Flatshring</h2>
  <div class="faq"><b>1.</b>Lorem Ipsum is simply dummy text of the printing and typesetting industry. Lorem Ipsum has been the industry's standard dummy text ever since the 1500s, when an unknown printer took a galley of type and scrambled it to make a type<span class="read-more">READ MORE &#8250;</span></div>
  <div class="faq-sep"></div>
  <div class="faq"><b>2.</b>Lorem Ipsum is simply dummy text of the printing and typesetting industry. Lorem Ipsum has been the industry's standard dummy text ever since the 1500s, when an unknown printer took a galley of type and scrambled it to make a type<span class="read-more">READ MORE &#8250;</span></div>
  <div class="faq-sep"></div>
  <div class="faq"><b>3.</b>Lorem Ipsum is simply dummy text of the printing and typesetting industry. Lorem Ipsum has been the industry's standard dummy text ever since the 1500s, when an unknown printer took a galley of type and scrambled it to make a type<span class="read-more">READ MORE &#8250;</span></div>
</section>

<div class="abs tab-teal"><span>TOOLS AND INFORMATIONS</span></div>
<div class="abs tab-green">PRE-DEFINED SEARCHES</div>

<footer class="abs site-footer">
  <div class="f-col" style="left:252px">
    <h4>COME VISIT US</h4>
    <p>Let's start talking about your project or idea and find out how we can help your business grow.</p>
    <address>14 Willow Crest Road,<br>Brightmoor Bay,<br>Halden County</address>
  </div>
  <div class="f-col" style="left:487px">
    <h4>MORE ABOUT US</h4>
    <p>Duis aliquet egestas purus in blandit. Curabitur vulputate, ligula lacinia scelerisque tempor, lacus lacus ornare ante, ac egestas est urna sit amet arcu. Class aptent taciti sociosqu ad litora lorem ipsum dolor sit amet scipitur nullam in dui mauris.</p>
  </div>
  <div class="f-col" style="left:721px">
    <h4>PHOTO FEED</h4>
    <div class="thumbs" role="img" aria-label="Grid of eight travel and city photos">
      <i style="background:linear-gradient(#7d8fa8,#a8845e)"></i><i style="background:linear-gradient(#3f6f7a,#c0473c)"></i><i style="background:linear-gradient(#2e6a6a,#86a7a0)"></i><i style="background:linear-gradient(#c98c4a,#3b4a78)"></i>
      <i style="background:linear-gradient(#8a9aa6,#5c4c3a)"></i><i style="background:linear-gradient(#5a8fb8,#d8b88a)"></i><i style="background:linear-gradient(#e3b46a,#7a5a3a)"></i><i style="background:linear-gradient(#4a3f5a,#d08a4a)"></i>
    </div>
  </div>
</footer>

<div class="abs bottom-nav">
  <nav><span class="active">Home</span><span>Group</span><span>Properties</span><span>Sales conditions</span><span>My account</span><span>Contact</span></nav>
  <div class="bottom-logo"><i></i>Lantern Nest Living</div>
</div>
<div class="abs copyright">Copyright © 2016 Lantern Nest Living</div>

</body>
</html>
```